Event website for the Brisk industry

brisk! is a new show in the Australian market so the website needs to be informative, easy to navigate and clear as to what the event is about and why they should attend – needs to be professional but still fun and dynamic.

Imagery needs to be colourful, fresh, inviting, and should involve a mixture of close up food shots with shots of people interacting.
The event’s competitions are fun and a little quirky (the “Toastathon” and “Blender Contest”), so creative should represent this in tone.

brisk! is a niche and unique show aimed at the multi-million dollar food-to-go market in Australia.
Key selling points for visitors:
- Discover the latest products (food and beverage lines) and equipment to hit the market
- Network with their peers
- Immerse themselves in a range of fun and interactive features – see attached list.
Key selling points for exhibitors:
- Speak directly to decision makers from small – large, food to go related businesses.
- Small niche show, exhibitors have more of an opportunity to stand out/ limited size so good variety of products on display

Some examples of Australian websites which are targeting the same type of customer:
http://www.wrapguild.org.au/ - clean/bright/simple
www.platterexpoaus.com.au – we like the simplicity of the Platter Expo website – very clean/colourful.
Updates

Hi All, 

Thanks for the interest in our competition, I will be away until the 11th of January at which point i will comment on the designs. 

Thanks and Merry Xmas. 

Target Market(s)

Café/Restaurant owners Sandwich bars/Juice Bars/Bakeries/Delis/Gourmet food stores Pubs/Clubs/Contract Caterers Supermarkets/Food Wholesalers

Industry/Entity Type

Industry

Requirements
Must have
• Main objectives:
1. Visitor Registration – call to action to "Register Now" needs to be very prominent on the home page and on the pages throughout the website
2. Information on exhibiting "Want to Exhibit" – needs to be clearly available.
3. Being a new show, data capture is important, so this needs to feature on the home page.
4. Social Media share buttons
5. Floating CSS Nav bar (top or bottom) with key call to actions - Register, Want to exhibit?, sign up

I would like all designs to have both a home page and a content page submitted.
Should not have
• Brisk UK show website: www.briskshow.co.uk
- We will be using the same branding as the UK brisk show website but we don’t like how busy their website is (too many blocks of run on text and too many navigation tiles on the home page). We would prefer to take a more simplified approach – ie. hero images (JQuery) dominating the screen, with a really strong CTA to register and to find out more about exhibiting.

```html
<!DOCTYPE html>
<html lang="en">
<head>
<meta charset="utf-8">
<title>brisk! – The contemporary food to go show</title>
<link rel="stylesheet" href="https://fonts.googleapis.com/css2?family=Archivo+Narrow:wght@400;500&family=Arimo:ital,wght@0,400;0,700;1,400&display=swap">
<style>
  :root {
    --green: #9cc23a;
    --green-light: #d9df7c;
    --ink: #111;
    --white: #fff;
    --rule: #dcdcdc;
  }
  * { box-sizing: border-box; margin: 0; padding: 0; }
  html, body { width: 1176px; height: 1200px; overflow: hidden; }
  body { background: var(--green); font-family: "Arimo", Arial, sans-serif; color: var(--ink); position: relative; }
  .page { position: absolute; left: 36px; top: 0; width: 1104px; height: 1200px; background: var(--white); }
  .navbar { position: absolute; left: 0; top: 34px; width: 1176px; height: 48px; background: linear-gradient(#2f2f2f, #161616); }
  .social { position: absolute; right: 48px; top: 12px; display: flex; align-items: center; gap: 6px; font-size: 13px; }
  .social span.label { margin-right: 6px; }
  .social i { display: block; width: 18px; height: 18px; border-radius: 3px; }
  .s1 { background: #3b5a9a; } .s2 { background: #36b6e6; } .s3 { background: #1b78b4; } .s4 { background: #f08a24; }
  .nav { position: absolute; top: 46px; left: 0; font-family: "Archivo Narrow", sans-serif; font-size: 20px; color: var(--white); }
  .nav a { position: absolute; white-space: nowrap; color: var(--white); text-decoration: none; }
  .nav a.active { color: #d6f27a; text-shadow: 0 0 8px rgba(200,240,90,.8); }
  .brand-name { position: absolute; left: 92px; top: 100px; display: flex; align-items: center; gap: 12px; font-family: "Arimo", sans-serif; font-weight: 700; font-size: 46px; line-height: 1; color: var(--ink); }
  .brand-name i { display: block; width: 18px; height: 18px; background: var(--green); }
  .event-info { position: absolute; right: 46px; top: 94px; text-align: right; color: var(--green); font-family: "Arimo", sans-serif; font-size: 21px; line-height: 27px; }
  .event-info small { display: block; font-size: 13px; line-height: 14px; }
  .hero { position: absolute; left: 36px; top: 176px; width: 1104px; height: 370px; background: radial-gradient(ellipse at 30% 50%, #e8e29a 0%, #b9c258 35%, #8ea43c 65%, #c2d7a8 100%); }
  .hero-panel { position: absolute; left: 584px; top: 64px; width: 480px; height: 234px; background: rgba(190,210,90,.45); border: 2px solid rgba(200,230,80,.8); padding: 28px 20px; font-family: "Archivo Narrow", sans-serif; font-size: 25px; line-height: 29px; text-align: center; color: #1a1a1a; }
  .hero-panel .brand { color: var(--white); }
  .register { display: block; width: 206px; height: 52px; margin: 20px auto 0; background: linear-gradient(#b6df56, #86b52c); border-radius: 3px; font-size: 27px; line-height: 52px; color: #222; box-shadow: 0 2px 6px rgba(0,0,0,.3); }
  .arrow { position: absolute; top: 338px; width: 56px; height: 66px; background: #111; }
  .arrow svg { position: absolute; left: 14px; top: 16px; }
  .arrow.prev { left: 16px; } .arrow.next { left: 1104px; }
  .intro { position: absolute; left: 56px; top: 580px; width: 760px; text-align: center; font-size: 26px; line-height: 26px; }
  .intro em { display: block; color: var(--green); font-size: 26px; margin-top: 2px; }
  .intro em b { color: var(--ink); font-style: normal; font-weight: 400; }
  .curve { position: absolute; left: 36px; top: 680px; }
  .about { position: absolute; left: 56px; top: 730px; width: 760px; font-size: 13.5px; line-height: 25px; }
  .about h2 { font-size: 19px; font-weight: 400; margin-bottom: 4px; }
  .strip { position: absolute; left: 56px; top: 936px; display: flex; height: 104px; }
  .strip .photo { height: 104px; }
  .strip .cta { width: 162px; background: var(--green); color: var(--white); padding: 22px 12px; font-size: 13px; }
  .strip .cta span { color: #111; }
  .strip .cta small { display: block; margin-top: 14px; font-size: 10.5px; line-height: 15px; }
  .closing { position: absolute; left: 56px; top: 1060px; width: 720px; font-size: 13.5px; line-height: 18px; }
  .divider { position: absolute; left: 836px; top: 600px; width: 1px; height: 560px; background: var(--rule); }
  .side { position: absolute; left: 852px; width: 272px; }
  .side h3 { font-size: 21px; font-weight: 400; }
  .side h3 span { color: var(--green); }
  .side p { font-size: 13.5px; line-height: 18px; color: #333; }
  .side .photo { width: 272px; }
  .signup { display: block; height: 44px; margin-top: 8px; background: linear-gradient(#a8d84a, #7fb02a); border-radius: 3px; text-align: center; font-family: "Archivo Narrow", sans-serif; font-size: 29px; line-height: 44px; color: #222; }
  .rule { height: 4px; background: #eee; margin: 14px 0 0; }
  .readmore { position: absolute; left: 1020px; top: 1118px; color: var(--green); font-size: 13.5px; font-weight: 700; display: flex; align-items: center; gap: 6px; }
  .footer { position: absolute; left: 36px; top: 1162px; width: 1104px; height: 38px; background: var(--green-light); text-align: center; font-size: 11px; line-height: 38px; }
</style>
</head>
<body>
  <div class="page"></div>
  <div class="navbar"></div>

  <div class="social"><span class="label">Find us on :</span><i class="s1"></i><i class="s2"></i><i class="s3"></i><i class="s4"></i></div>

  <nav class="nav">
    <a class="active" style="left:576px">Home</a>
    <a style="left:686px">About us</a>
    <a style="left:811px">Exhibitors</a>
    <a style="left:942px">Events</a>
    <a style="left:1038px">Contact</a>
  </nav>

  <div class="brand-name"><i></i>brisk!</div>

  <div class="event-info">
    6th-7th August 2010,<br>
    Grand Hall of Trades, Harbour Park Sydney
    <small>www.briskshow.com.au</small>
  </div>

  <section class="hero" role="img" aria-label="Close-up photo of a kiwi fruit smoothie with ice and a kiwi slice">
    <div class="hero-panel">
      <span class="brand">brisk!</span> brings together the flavorful talents through the Smoothie Challenge 2012.<br>
      Join the rendezvous of fun,food and amazing people!!!
      <span class="register">Register Now</span>
    </div>
  </section>
  <div class="arrow prev"><svg width="28" height="34" viewBox="0 0 28 34"><path d="M20 2 6 17l14 15" fill="none" stroke="#fff" stroke-width="4"/></svg></div>
  <div class="arrow next"><svg width="28" height="34" viewBox="0 0 28 34"><path d="M8 2l14 15L8 32" fill="none" stroke="#fff" stroke-width="4"/></svg></div>

  <div class="intro">
    Australia’s first dedicated trade event for the food-to-go market.
    <em>Lets go <b>brisk!</b> together in 2012</em>
  </div>
  <svg class="curve" width="800" height="30" viewBox="0 0 800 30"><path d="M0 16 Q400 -6 800 16 Q400 6 0 16Z" fill="#e6e6e6"/></svg>

  <section class="about">
    <h2>Whats brisk! all about?</h2>
    <p>brisk! Australia's first dedicated trade event for the multi-million dollar food-to-go market.brisk! Grand Hall of Trades, Harbour Park, Sydney on 6-7 August 2012. brisk! developed in close consultation with leading industry suppliers, retailers and associations.<br>
    brisk! an unmissable opportunity for owners and managers of quality sandwich bars, juice bars, cafes, restaurants, hotels, delicatessens and contract caterers to source new products and innovations, find out about the latest food-to-go market trends and network with 1000’s of industry professionals all in one dedicated arena.</p>
  </section>

  <div class="strip">
    <div class="photo" style="width:157px;background:linear-gradient(135deg,#6f8a3a,#c79a5a)" role="img" aria-label="Photo of friends sharing lunch at an outdoor cafe"></div>
    <div class="photo" style="width:169px;background:linear-gradient(135deg,#d8d0c0,#8a8878)" role="img" aria-label="Photo of people chatting over food"></div>
    <div class="photo" style="width:92px;background:linear-gradient(135deg,#8a3a2a,#d0a080)" role="img" aria-label="Photo of a group dining together"></div>
    <div class="photo" style="width:170px;background:linear-gradient(135deg,#7a9a4a,#d8d2c0)" role="img" aria-label="Photo of a picnic on the grass"></div>
    <div class="cta">Everyone loves <span>brisk!</span><small>Tell me more about the Events ➤</small></div>
  </div>

  <p class="closing">Along with a dedicated brisk! exhibitor zone, the brisk! menu will be packed with tasty features and attractions, including: stimulating speakers, exciting demonstrations, dynamic competitions and informative workshops.</p>

  <div class="divider"></div>

  <aside class="side" style="top:586px">
    <h3>Want to exhibit at <span>brisk!</span></h3>
    <p style="padding-left:26px;margin-top:4px">Be part of this exciting new trade event.Book your stand today!</p>
    <div class="photo" style="height:148px;margin-top:10px;background:linear-gradient(135deg,#e8e4e0,#b87a60 60%,#6a6a6a)" role="img" aria-label="Photo of a chef plating a dessert"></div>
    <span class="signup">Sign up</span>
    <div class="rule"></div>
    <h3 style="margin-top:14px">Exhibitor Services</h3>
    <p style="padding-left:4px">Exhibitor forms rules ,deadlines and more</p>
    <div class="photo" style="height:148px;margin-top:8px;background:linear-gradient(135deg,#d8c8b0,#c08050 55%,#f0ece8)" role="img" aria-label="Photo of two chefs cooking in a kitchen"></div>
  </aside>
  <div class="readmore">Read More <svg width="16" height="14" viewBox="0 0 16 14"><path d="M0 0l16 7L0 14l4-7z" fill="#9cc23a"/></svg></div>

  <footer class="footer">Copyright © 2011 brisk!</footer>
</body>
</html>
```